Business Card Design Project

I am opening a skin care studio called Glow Bloom by Marisa. I will be offering a wide range of unique and affordable skin services including facials, chemical peels, microdermabrasion treatments, body wraps, salt glows, all waxing and eye lash extensions. If the business cards depicts what I would like, this would lead to brochures, web design, signs, etc.
Updates

Project Deadline Extended
Reason: A request to extend deadline was requested. I will be more than happy to accommodate.

Industry/Entity Type

Business

Requirements
Nice to have
• facial features so prospective client clearly identifies what type of business this is. Not stuffy or boring "spa" looking graphics. I am focusing just on face, body, waxing, eyelashes. No massage or nails.

```html
<!DOCTYPE html>
<html lang="en">
<head>
<meta charset="utf-8">
<title>Glow Bloom by Marisa – Business Card</title>
<link rel="stylesheet" href="https://fonts.googleapis.com/css2?family=Pinyon+Script&family=Questrial&display=swap">
<style>
  :root {
    --page: #ffffff;
    --lavender-deep: #c7b4da;
    --lavender-soft: #e5cde6;
    --blush-white: #fdf6f9;
    --plum: #5e3f6e;
    --plum-soft: #7a5a88;
    --shadow: rgba(60, 40, 70, 0.22);
  }
  * { box-sizing: border-box; margin: 0; padding: 0; }
  html, body {
    width: 1200px; height: 900px; overflow: hidden;
    background: var(--page);
  }
  .canvas { position: relative; width: 1200px; height: 900px; }

  .card {
    position: absolute;
    box-shadow: 0 6px 14px var(--shadow);
    overflow: hidden;
  }
  .card--front { left: 40px; top: 304px; width: 528px; height: 322px; background: var(--lavender-soft); }
  .card--back  { left: 632px; top: 312px; width: 530px; height: 324px; background: var(--blush-white); }

  .card__waves { position: absolute; inset: 0; width: 100%; height: 100%; }

  .brand {
    position: absolute;
    font-family: "Questrial", sans-serif;
    font-weight: 400;
    color: var(--plum);
    line-height: 1.05;
  }
  .brand__name { display: block; font-size: 44px; letter-spacing: 0.5px; }
  .brand__by { display: block; font-size: 20px; padding-left: 150px; }
  .brand__dot {
    position: absolute; top: -4px; width: 14px; height: 14px;
    border-radius: 50%; background: var(--plum-soft);
  }
  .card--front .brand { left: 70px; top: 86px; }
  .card--front .brand__dot { left: 232px; }
  .card--back .brand { left: 40px; top: 60px; }
  .card--back .brand__dot { left: 232px; }

  .tagline {
    position: absolute; left: 0; right: 0; top: 228px;
    text-align: center;
    font-family: "Pinyon Script", cursive;
    font-size: 30px; line-height: 1.05;
    color: var(--plum);
  }
  .tagline__accent {
    position: absolute; width: 10px; height: 10px; top: 268px;
    background: var(--plum-soft); opacity: 0.55; border-radius: 50%;
  }
  .tagline__accent--left { left: 122px; }
  .tagline__accent--right { left: 400px; top: 264px; }

  .contact {
    position: absolute; left: 36px; top: 160px;
    font-family: "Questrial", sans-serif;
    color: var(--plum);
  }
  .contact__name { font-size: 24px; margin-bottom: 12px; }
  .contact__line { font-size: 17px; line-height: 28px; }
  .contact__web {
    position: absolute; left: 0; right: 0; top: 280px;
    text-align: center;
    font-family: "Questrial", sans-serif;
    font-size: 17px; letter-spacing: 0.6px;
    color: var(--plum);
  }
</style>
</head>
<body>
<main class="canvas">

  <section class="card card--front" aria-label="Business card front">
    <svg class="card__waves" viewBox="0 0 528 322" preserveAspectRatio="none" aria-hidden="true">
      <path d="M0,0 H528 V62 C330,40 140,44 0,100 Z" fill="var(--lavender-deep)"/>
      <path d="M0,100 C140,44 330,40 528,62 L528,150 C430,168 300,150 210,172 C140,190 70,205 0,200 Z" fill="var(--blush-white)"/>
    </svg>
    <div class="brand">
      <span class="brand__dot"></span>
      <span class="brand__name">Glow Bloom</span>
      <span class="brand__by">by Marisa</span>
    </div>
    <p class="tagline">For all your beauty<br>and skin care needs</p>
    <span class="tagline__accent tagline__accent--left" role="img" aria-label="Small heart ornament"></span>
    <span class="tagline__accent tagline__accent--right" role="img" aria-label="Small heart ornament"></span>
  </section>

  <section class="card card--back" aria-label="Business card back">
    <div class="brand">
      <span class="brand__dot"></span>
      <span class="brand__name">Glow Bloom</span>
      <span class="brand__by">by Marisa</span>
    </div>
    <div class="contact">
      <p class="contact__name">Marisa</p>
      <p class="contact__line">Address: 418 Elm Avenue Fairview, CO 80999</p>
      <p class="contact__line">Phone: 970-555-0142</p>
    </div>
    <p class="contact__web">glowbloombymarisa.com</p>
  </section>

</main>
</body>
</html>
```